Business Card Design

Hi I need a business card designed, we already have the business name logo artwork and would like some concept ideas for the Bus Card layout.
On the back of the card i want to include the products and services that we offer.
We are a Plastics Sheeting manufacture based in Perth Australia.

                                       

We need a BC design for a company called Tarnby Plastics based in Perth Australia.

We supply from DIY to Trade & Industrial  Engineering Markets.

We specialise in:

·         Cut to size panels  (all shapes and sizes)

·         Plastics fabrication & Welding

·         Custom Designs

·         Plastic Repairs

·         PVC Pipe Slotting & PVC Pipe Threading

·         Supplier of all types of engineering plastics and profiles.

Including:           Acrylic / Vendrix

                               Polycarbonate / Moravite

                               Prismatic Light Diffuser

                               Tubrasin

                               HDPE / UHMWPE

                               PVC / PVC Foam

                               Nylon

                               HIPS

```html
<!DOCTYPE html>
<html lang="en">
<head>
<meta charset="utf-8">
<title>Tarnby Plastics – Business Card</title>
<link href="https://fonts.googleapis.com/css2?family=Arimo:ital,wght@0,400;0,700;1,700&display=swap" rel="stylesheet">
<style>
  :root {
    --backdrop: #3b2c22;
    --card-white: #ffffff;
    --brand-navy: #1b2a5c;
    --brand-green: #4b8c2a;
    --link-blue: #2a8fd0;
    --band-red: #c8202e;
    --band-orange: #e8731e;
    --band-yellow: #f2b418;
    --band-blue: #2a8fd0;
    --band-green: #4b8c2a;
    --text-white: #ffffff;
  }
  * { box-sizing: border-box; margin: 0; padding: 0; }
  html, body { width: 1200px; height: 631px; overflow: hidden; }
  body {
    background: var(--backdrop);
    font-family: "Arimo", Arial, sans-serif;
    position: relative;
  }
  .card {
    position: absolute;
    top: 150px;
    width: 540px;
    height: 330px;
    border-radius: 3px;
    overflow: hidden;
  }
  /* Back side */
  .card--back { left: 40px; background: var(--brand-green); color: var(--text-white); }
  .card--back .wordmark {
    position: absolute; top: 30px; right: 30px;
    font-size: 30px; font-weight: 700; color: var(--text-white);
  }
  .services { position: absolute; left: 30px; top: 96px; width: 300px; font-size: 10.5px; line-height: 17px; }
  .services .intro { margin-bottom: 4px; white-space: nowrap; }
  .services h2 { font-size: 10.5px; font-weight: 700; }
  .services ul { list-style: none; }
  .services li { white-space: nowrap; }
  .services li::before { content: "• "; }
  .materials { position: absolute; left: 345px; top: 96px; font-size: 10.5px; line-height: 17px; font-weight: 700; }
  .materials h2 { font-size: 10.5px; font-style: italic; font-weight: 700; }
  .materials ul { list-style: none; }

  /* Front side */
  .card--front { left: 620px; background: var(--card-white); color: var(--brand-navy); }
  .edge-bands { position: absolute; left: 0; top: 0; width: 14px; height: 330px; }
  .person { position: absolute; left: 48px; top: 78px; font-size: 16px; line-height: 20px; }
  .person .name, .person .role { font-weight: 700; }
  .card--front .wordmark {
    position: absolute; left: 48px; top: 186px;
    font-size: 24px; font-weight: 700; color: var(--brand-navy);
    white-space: nowrap;
  }
  .divider { position: absolute; left: 262px; top: 40px; width: 20px; height: 240px; }
  .contact { position: absolute; left: 292px; top: 52px; font-size: 14px; line-height: 21px; white-space: nowrap; }
  .contact strong { font-weight: 700; }
  .contact .email { color: var(--link-blue); }
  .legal { position: absolute; left: 292px; top: 222px; font-size: 8px; letter-spacing: 0.2px; white-space: nowrap; }
</style>
</head>
<body>
  <section class="card card--back" aria-label="Card back">
    <div class="wordmark">Tarnby Plastics</div>
    <div class="services">
      <p class="intro">We supply from DIY to Trade &amp; Industrial Engineering Markets.</p>
      <h2>We specialise in:</h2>
      <ul>
        <li>Cut to size panels (all shapes and sizes)</li>
        <li>Plastics fabrication &amp; Welding</li>
        <li>Custom Designs</li>
        <li>Plastic Repairs</li>
        <li>PVC Pipe Slotting &amp; PVC Pipe Threading</li>
        <li>Supplier of all types of engineering plastics and profiles.</li>
      </ul>
    </div>
    <div class="materials">
      <h2>Including</h2>
      <ul>
        <li>Acrylic / Vendrix</li>
        <li>Polycarbonate / Moravite</li>
        <li>Prismatic Light Diffuser</li>
        <li>Tubrasin</li>
        <li>HDPE / UHMWPE</li>
        <li>PVC / PVC Foam</li>
        <li>Nylon</li>
        <li>HIPS</li>
      </ul>
    </div>
  </section>

  <section class="card card--front" aria-label="Card front">
    <svg class="edge-bands" viewBox="0 0 14 330" aria-hidden="true">
      <rect x="0" y="0" width="6" height="66" fill="var(--band-red)"/>
      <rect x="0" y="66" width="8" height="66" fill="var(--band-orange)"/>
      <rect x="0" y="132" width="10" height="66" fill="var(--band-yellow)"/>
      <rect x="0" y="198" width="8" height="66" fill="var(--band-blue)"/>
      <rect x="0" y="264" width="6" height="66" fill="var(--band-green)"/>
    </svg>
    <div class="person">
      <p class="name">Dale Hensley</p>
      <p class="phone">0400 555 218</p>
      <p class="role">Manager</p>
    </div>
    <div class="wordmark">Tarnby Plastics</div>
    <svg class="divider" viewBox="0 0 20 240" aria-hidden="true">
      <polyline points="4,0 4,108 12,118 4,128 4,240" fill="none" stroke="var(--brand-navy)" stroke-width="1.5"/>
    </svg>
    <div class="contact">
      <p>Unit 4/18 Kestrel</p>
      <p>Circuit Norvale WA 6160</p>
      <p>Ph: <strong>08 9471 3308</strong> Fax: <strong>08 9471 3309</strong></p>
      <p>E: <span class="email">sales@tarnbyplastics.com.au</span></p>
      <p>PO Box 2274 Norvale DC WA 6971</p>
    </div>
    <p class="legal">HARROWELL WA Pty Ltd T/A Tarnby Plastics ABN: TBA</p>
  </section>
</body>
</html>
```